Corporate services company needs a brochure

We are starting a company offering setup services to companies new to that location.
This includes services such as recruitment, company formation, advertising, marketing, pr, handling legal issues, logistics, transportation, procurement,immigration services, corporate gifts, accomodation,entertainment, training, administrative services etc.
Basically taking the setup issues off the hands of the company allowing them focus on their core business.

We are looking to design a professional brochure which would give the potential customers the confidence to entrust us with their needs.

We will be including some copy that can be used but i would very much like for you to bring what i have written to life - adding, deducting and amending where required.

We are looking at a A4 4/6 paged brochure but open to suggestions.

                                       

If you have any images that are suitable, please let us know. We will also be searching for some to add.

The first prize has been increased.

Thanks

Reason: We have just guaranteed the payment and we are hoping that this will encourage good designers to participate.

Reason: Some designers have requested more time to complete their final design.

Hi, I h extended the deadline to give designers more time to work on designs.

we are also looking at making the brochure a height of 8.5 and a width of 11. Please let me know your thoughts on this as any advice will help. The whole objective is to make it look as up to date and creative as possible. There is also another design size of 7.5 by 8.5

Thanks

                                        Hi

The copy has been revised and uploaded.

Hopefully it will give a clearer explanation of what we are trying to do.

Please let me know if you have any further questions.

Thanks

Marta

Reason: adding finishing touches to designs

Reason: We are amending the copy for the brochure

Reason: The new copy for the brochure is ready. I am sorry it has taken so long to get it out. I am sure we will not be making any amendments to it post today. Thanks for your patience The extension is not to attact new designs it is for existing designs's copy to be modified to include information from the updated copy.

Target Market(s)

medium to large companies in banking, telecom, retail etc. It will be viewed by middle and top management.

Industry/Entity Type

Legal

Requirements
Must have
• The brochure must clearly highlight all our services without just listing as this would risk it appearing as if we have just included everything we could think of!,
Please do not do the sitting round the conference table brochure or the typical blue and white brochure.
I desperately need it to be different, unique and serious enough to show that we are capable of handling/managing all what we have included.
Our clients include the many companies starting up an office in Africa.
We are anxious to have the potential clients understand that we will help them setup under any climax/
Nice to have
• modern colours but not too bright. there must still be a clear serious edge to it.
Should not have
• conference room table and people sitting around it.
the typical blue and white brochures often used for these type of services.

```html
<!DOCTYPE html>
<html lang="en">
<head>
<meta charset="utf-8">
<title>Varlo — Services</title>
<link rel="stylesheet" href="https://fonts.googleapis.com/css2?family=Open+Sans:wght@400;800&family=Source+Sans+3:wght@400;700&display=swap">
<style>
:root{
  --night:#05070d;
  --deep-blue:#0c2a4a;
  --band-grey:#5b5d60;
  --orange:#ea6f34;
  --headline-orange:#f05a2a;
  --red:#e81c24;
  --white:#ffffff;
}
*{margin:0;padding:0;box-sizing:border-box}
html,body{width:929px;height:1200px;overflow:hidden;background:var(--night)}
body{font-family:"Source Sans 3","Myriad Pro",Arial,sans-serif;color:var(--white)}
.page{position:relative;width:929px;height:1200px;overflow:hidden}
.backdrop{position:absolute;inset:0;
  background:
    radial-gradient(circle at 55% 22%, rgba(47,111,158,.75) 0, rgba(47,111,158,0) 28%),
    radial-gradient(circle at 85% 45%, rgba(38,95,140,.7) 0, rgba(38,95,140,0) 30%),
    radial-gradient(circle at 15% 15%, rgba(30,80,120,.6) 0, rgba(30,80,120,0) 25%),
    radial-gradient(circle at 70% 70%, rgba(20,70,110,.55) 0, rgba(20,70,110,0) 30%),
    linear-gradient(180deg,#04060b 0%,var(--deep-blue) 45%,#06101c 100%);}
.brand-band{position:absolute;top:83px;height:57px;background:var(--band-grey);opacity:.85}
.brand-band.left{left:0;width:332px}
.brand-band.right{left:612px;width:317px}
.brand-name{position:absolute;top:62px;left:332px;width:280px;text-align:center;
  font-family:"Open Sans",Arial,sans-serif;font-weight:400;font-size:78px;line-height:100px;letter-spacing:2px;color:var(--white)}
.outline-shape{position:absolute;left:0;top:0}
.headline{position:absolute;font-family:"Open Sans",Arial,sans-serif;font-weight:800;color:var(--headline-orange);letter-spacing:-2px;line-height:1}
.headline.services{left:40px;top:210px;font-size:122px}
.headline.benefits{left:602px;top:644px;font-size:56px;color:var(--red);letter-spacing:-1px}
.panel{position:absolute}
.panel.services-panel{left:24px;top:318px;width:549px;height:882px;background:var(--orange)}
.panel.benefits-panel{left:600px;top:688px;width:329px;height:512px;background:var(--red)}
.column{position:absolute;font-size:13px;line-height:15.5px;hyphens:auto;-webkit-hyphens:auto}
.column p{text-align:justify}
.column .gap{margin-top:15.5px}
.column .gap-2{margin-top:31px}
.column h3{font-size:12.5px;font-weight:700;line-height:15.5px;text-transform:uppercase}
.column ul{list-style:none}
.column li{padding-left:11px;position:relative}
.column li::before{content:"•";position:absolute;left:0}
.col-left{left:44px;top:341px;width:240px}
.col-right{left:301px;top:356px;width:257px}
.col-benefits{left:615px;top:709px;width:278px}
</style>
</head>
<body>
<div class="page">
  <div class="backdrop" role="img" aria-label="Dark blue background with soft glowing bokeh lights"></div>

  <div class="brand-band left"></div>
  <div class="brand-band right"></div>
  <div class="brand-name">varlo</div>

  <svg class="outline-shape" width="929" height="1200" viewBox="0 0 929 1200" aria-hidden="true">
    <path d="M4 300 L18 238 Q24 214 50 212 L566 212 Q592 214 590 240 L582 318 L4 318 Z" fill="#fff"/>
    <path d="M592 690 L604 644 Q608 632 624 632 L872 632 Q892 634 888 652 L876 690 Z" fill="#fff"/>
  </svg>

  <div class="headline services">SERVICES</div>

  <div class="panel services-panel"></div>
  <div class="panel benefits-panel"></div>
  <div class="headline benefits">BENEFITS</div>

  <div class="column col-left">
    <p>It is a strategic partnership that ensures that we'll always deliver the finest and most appropriate business infrastructure solutions required to reach your goals and achieve your ongoing success.</p>
    <div class="gap">Business services</div>
    <ul><li>Logos</li><li>Brochures</li><li>Letterhead</li><li>Signage</li></ul>
    <div>Web/IT Services</div>
    <ul><li>Web design/development</li><li>Search engine optimization and market&shy;ing services</li><li>Remote help desk – email/call forming</li><li>Custom web applications</li><li>Network setup</li></ul>
    <h3 class="gap">Who hires us?</h3>
    <p class="gap">Varlo provides managed, business services to companies in all stages of development, from early start-ups to corporations starting new in country that require a broad range of expertise to large well established corpora&shy;tions that simply need help completing an essential project in a hurry and on a budget.</p>
    <p class="gap">Our professionals fulfill critical roles in all stages of development and manage those functions in association with our clients. We manage the tasks and talent necessary for tactical success so you can concentrate on your strategic goals.</p>
    <p class="gap">We offer a cost effective way to immediately hire the unique combination of expertise required to manage and help your business surge ahead of the competition.</p>
    <p>We'll always deliver the smartest and most cost effective business infrastructure solutions required to reach your goals and achieve ongoing success.</p>
    <p class="gap">We are a 'one-stop' shop for startups – whether you're still in slide-deck modes or further along in the process of starting your new venture, we have services that fit your needs.</p>
  </div>

  <div class="column col-right">
    <p>No matter the stage of your company, our services and expertise can help you drive your business forward. If you require consultation with other entrepreneurs and also need the services we provide, we will construct a plan that includes both. Our goal is to customize an approach that matches your interests, blends in the advice of business people who have had success and offer operational expertise to perform the tasks that will get your enterprise running smoothly.</p>
    <h3 class="gap">Start-up services</h3>
    <div>General Services</div>
    <div>Business plan (Review and writing)</div>
    <div>Web development</div>
    <div>Logo design</div>
    <div>Network/IT step and maintenance</div>
    <div>Phone systems</div>
    <p>Office building (office partitioning, structured cabling, office furniture etc.)</p>
    <div>Advertising</div>
    <div>Cabling</div>
    <div>Accounts/Bookkeeping/Payroll/Contractors</div>
    <div>Legal</div>
    <h3 class="gap">Human resources services</h3>
    <div>HR function set-up</div>
    <div>Employee handbooks and policies</div>
    <div>Employee Performance Management</div>
    <div>HR hotline</div>
    <div>Job description</div>
    <div>Phone screening</div>
    <div>Staff screening (referencing and health)</div>
    <div>Offer letters</div>
    <div>Training</div>
    <div>Job posting</div>
    <div>Recruitment.</div>
    <p class="gap">It is a strategic partnership that will ensure that well always deliver the smartest and most cost-effective business infrastructure solutions required to reach your goals and achieve ongoing success.</p>
  </div>

  <div class="column col-benefits">
    <h3>Benefit from our economies of scale</h3>
    <p>We buy on behalf of our many clients, so whether you need hotel rooms, car rentals or advertising services our buying power and experience ensures that it will always get the best quality services at the lowest price.</p>
    <div class="gap-2" style="margin-top:46px">Virtual office package</div>
    <p>Mail handling, the answering of phone calls in your company name, the use of a local business address in a prestige location.</p>
    <div>Concierge</div>
    <div>What your concierge can help with:</div>
    <p>Entertainment, travel, house comforts, personal shopping, relaxation, cars and transportation, personal and business storage, corporate gifts.</p>
    <p class="gap">Varlo is a full-service business development group and general management consultancy firm focused on small and medium sized privately held companies in Africa.</p>
    <p class="gap-2">At Varlo, we deeply care for our clients, firmly believe our people and take pride in what we do.</p>
  </div>
</div>
</body>
</html>
```